IT services company requires Letterhead design

We need a professional letterhead designed to be used for general correspondence with customers, quotes, invoices etc. We are a new IT services company specialising in computer servicing and repairs and mobile and tablet repairs. Attached are templates that my printing company have supplied, my logos, an interpretation of our website for you to get a feel of the company. Details to be included on the letterhead are

Company Number – 4738261
VAT Number - 518337942
Registered Address – 14-16 Brambly Lane, London, E4 9QT

Phone – 01632 487215
Email – sales@quorvent.com
Web – www.quorvent.com

I would prefer for the top of the letterhead to just have the company logo on a white background and the rest of the details on the bottom of the letterhead but I am open to design ideas.

Thanks

```html
<!DOCTYPE html>
<html lang="en">
<head>
<meta charset="utf-8">
<title>Quorvent Letterhead</title>
<link rel="stylesheet" href="https://fonts.googleapis.com/css2?family=Open+Sans:wght@600;700&display=swap">
<style>
  :root {
    --brand-cyan: #2cc1e1;
    --ink-dark: #3a3a3c;
    --paper: #ffffff;
    --footer-text: #2f3336;
  }
  html, body {
    margin: 0;
    padding: 0;
    overflow: hidden;
    background: var(--paper);
  }
  .letterhead {
    position: relative;
    width: 849px;
    height: 1200px;
    background: var(--paper);
    overflow: hidden;
    font-family: "Open Sans", Arial, sans-serif;
  }
  .brand-mark {
    position: absolute;
    left: 56px;
    top: 92px;
    display: flex;
    align-items: center;
    gap: 12px;
  }
  .brand-mark__square {
    width: 22px;
    height: 22px;
    background: var(--brand-cyan);
  }
  .brand-mark__name {
    font-size: 44px;
    font-weight: 700;
    color: var(--ink-dark);
    letter-spacing: -0.5px;
    line-height: 1;
  }
  .footer-band {
    position: absolute;
    left: 0;
    top: 919px;
    width: 849px;
    height: 281px;
    background: var(--brand-cyan);
  }
  .footer-notch {
    position: absolute;
    left: 0;
    top: 919px;
  }
  .footer-mark {
    position: absolute;
    right: 52px;
    top: 958px;
    display: flex;
    align-items: center;
    gap: 9px;
  }
  .footer-mark__square {
    width: 14px;
    height: 14px;
    background: var(--paper);
  }
  .footer-mark__name {
    font-size: 30px;
    font-weight: 700;
    color: var(--paper);
    line-height: 1;
  }
  .company-details {
    position: absolute;
    left: 53px;
    top: 1012px;
    margin: 0;
    font-size: 15.5px;
    font-weight: 600;
    line-height: 18.5px;
    color: var(--footer-text);
  }
  .contact-row {
    position: absolute;
    left: 0;
    top: 1104px;
    width: 849px;
    height: 36px;
  }
  .contact-item {
    position: absolute;
    top: 0;
    height: 36px;
    display: flex;
    align-items: center;
    gap: 14px;
    color: var(--paper);
    font-size: 18.5px;
    font-weight: 600;
  }
  .contact-item svg { display: block; }
  .contact-item--phone { left: 62px; gap: 20px; }
  .contact-item--email { left: 322px; }
  .contact-item--web { left: 600px; }
  .contact-divider {
    position: absolute;
    top: 3px;
    width: 2px;
    height: 29px;
    background: var(--paper);
  }
  .contact-divider--first { left: 291px; }
  .contact-divider--second { left: 572px; }
</style>
</head>
<body>
<div class="letterhead">
  <div class="brand-mark">
    <span class="brand-mark__square"></span>
    <span class="brand-mark__name">Quorvent</span>
  </div>

  <div class="footer-band"></div>
  <svg class="footer-notch" width="849" height="60" viewBox="0 0 849 60" aria-hidden="true">
    <polygon points="68,0 164,0 116,52" fill="#ffffff"/>
  </svg>

  <div class="footer-mark">
    <span class="footer-mark__square"></span>
    <span class="footer-mark__name">Quorvent</span>
  </div>

  <p class="company-details">
    Registered Address – 14-16 Brambly Lane, London, E4 9QT<br>
    Company Number – 4738261<br>
    VAT Number - 518337942
  </p>

  <div class="contact-row">
    <div class="contact-item contact-item--phone">
      <svg width="20" height="26" viewBox="0 0 20 26" aria-hidden="true">
        <path d="M5 1 L8.5 1 L10 7 L7.5 9 C8.5 12.5 10 15.5 12.5 18 L15 16.5 L19 20.5 L17 24.5 C10 25 2 15 2 5 Z" fill="#ffffff"/>
      </svg>
      <span>01632 487215</span>
    </div>
    <span class="contact-divider contact-divider--first"></span>
    <div class="contact-item contact-item--email">
      <svg width="28" height="20" viewBox="0 0 28 20" aria-hidden="true">
        <rect x="1" y="1" width="26" height="18" fill="none" stroke="#ffffff" stroke-width="1.8"/>
        <path d="M1 1 L14 11 L27 1 M1 19 L10.5 8.5 M27 19 L17.5 8.5" fill="none" stroke="#ffffff" stroke-width="1.6"/>
      </svg>
      <span>sales@quorvent.com</span>
    </div>
    <span class="contact-divider contact-divider--second"></span>
    <div class="contact-item contact-item--web">
      <svg width="22" height="22" viewBox="0 0 22 22" aria-hidden="true">
        <circle cx="11" cy="11" r="9.5" fill="none" stroke="#ffffff" stroke-width="1.8"/>
        <ellipse cx="11" cy="11" rx="4.2" ry="9.5" fill="none" stroke="#ffffff" stroke-width="1.5"/>
        <path d="M1.5 11 H20.5 M3.5 6 H18.5 M3.5 16 H18.5" stroke="#ffffff" stroke-width="1.4"/>
      </svg>
      <span>www.quorvent.com</span>
    </div>
  </div>
</div>
</body>
</html>
```